Flyer for International Internship Program in Dublin, Ireland

We need a one-page flyer promoting our newest internship program in Dublin, Ireland called "Venture Lantern". Northbound Placements provides international internship programs (like a study abroad) for university students. The Venture Lantern program is 10 weeks and includes full-time internship in an Irish start-up company, panel discussions with entrepreneurs and industry leaders, and a business competition along with social events and housing in Dublin. The flyer must convey the purpose of the program to university students as well as be fun and professional.
Updates

I've posted a new logo in .png format. Please let me know if there are any issues with that file. 

We've made some changes to text:

1. Please change the title to: 
Venture Lantern 
Dublin Entrepreneur Internship Program 

2. Please add the price: $7,190
3. Please add an Irish and American flag 
4. Please be sure that the color scheme is similar to that palette of the logo

Target Market(s)

We are trying to attract university students (21-23) as well as college staff like study abroad offices and advisors.

Industry/Entity Type

University

Requirements
Must have
• We would like to see flyers convey all of the content attached as well as images of Dublin, and business/professional themed photos. The flyer must have our logo (attached) and website. We'd like the information divided into sections so it looks clean and easy to read.
Nice to have
• We'd like to see some color (like our logo), but it doesn't need to be too bright or overwhelming. Young, but professional.
Should not have
• Do not use any overly styled fonts like scripts or "Celtic-looking" text.

```html
<!DOCTYPE html>
<html lang="en">
<head>
<meta charset="utf-8">
<title>Venture Lantern – Dublin Entrepreneur Internship Program</title>
<link href="https://fonts.googleapis.com/css2?family=Source+Sans+3:wght@400;600&display=swap" rel="stylesheet">
<style>
  :root{
    --bg-top:#4d8b8c;
    --bg-mid:#8fb8a8;
    --bg-low:#b7d2c3;
    --ink:#17474f;
    --ink-soft:#1f3a3e;
    --rule:#1b4750;
    --frame:#1a2c30;
    --white:#ffffff;
    --brand:#1f5f8b;
    --us-red:#c8313e;
    --us-blue:#2d3f7a;
    --ie-green:#169b62;
    --ie-orange:#ff883e;
  }
  *{box-sizing:border-box;margin:0;padding:0}
  html,body{width:785px;height:1200px;overflow:hidden}
  body{font-family:"Source Sans 3",Arial,sans-serif;color:var(--ink-soft)}
  .flyer{position:relative;width:785px;height:1200px;overflow:hidden;
    background:linear-gradient(180deg,var(--bg-top) 0%,#6fa39c 30%,var(--bg-mid) 55%,var(--bg-low) 100%)}
  .brand{position:absolute;left:6px;top:6px;width:222px;height:100px;background:var(--white);
    display:flex;align-items:center;justify-content:center;gap:10px}
  .brand-dot{width:30px;height:30px;border-radius:50%;background:var(--brand)}
  .brand-name{font-weight:600;font-size:19px;color:var(--brand);line-height:1.05;letter-spacing:.5px}
  .flag{position:absolute;top:9px;width:84px;height:84px}
  .flag-us{left:606px}
  .flag-ie{left:698px}
  .photo{position:absolute;border-radius:14px;border:3px solid var(--frame)}
  .photo-office{left:0;top:115px;width:205px;height:273px;background:linear-gradient(160deg,#a7c7de 0%,#8a6252 45%,#5b3d33 100%)}
  .photo-river{left:214px;top:115px;width:340px;height:273px;background:linear-gradient(180deg,#6f8fb6 0%,#b99a6a 45%,#2c3f45 70%,#1d3a38 100%)}
  .photo-hall{left:566px;top:115px;width:230px;height:273px;background:linear-gradient(180deg,#6e9bd0 0%,#c9c4b4 45%,#9a958a 80%,#6d6c63 100%)}
  .lines{position:absolute;left:0;top:0}
  .title{position:absolute;left:36px;top:412px;font-size:50px;font-weight:400;color:var(--ink);letter-spacing:.3px}
  .subtitle{position:absolute;left:36px;top:476px;font-size:31px;font-weight:400;color:var(--ink)}
  .dates{position:absolute;left:36px;top:514px;font-size:19px;color:var(--ink)}
  .col-why{position:absolute;left:36px;top:548px;width:250px}
  .col-exp{position:absolute;left:303px;top:548px;width:470px}
  h2{font-size:15.5px;font-weight:400;color:var(--ink-soft);margin-bottom:14px}
  p{font-size:15.4px;line-height:21px;color:var(--ink-soft)}
  .inclusions{margin-top:30px}
  ul{list-style:none}
  li{font-size:14.4px;line-height:20px}
  li::before{content:"•";margin-right:5px}
  .shot{position:absolute}
  .shot-team{left:36px;top:811px;width:233px;height:123px;background:linear-gradient(180deg,#d9dde0 0%,#8c8f8d 50%,#2f3a3c 100%)}
  .shot-lobby{left:36px;top:1009px;width:233px;height:135px;background:linear-gradient(160deg,#c6c97a 0%,#6f6a55 45%,#2b2b27 100%)}
  .shot-board{left:552px;top:1061px;width:221px;height:124px;background:linear-gradient(180deg,#c9c6bb 0%,#a89f8c 50%,#4a4540 100%)}
  .price{position:absolute;left:303px;top:985px;font-size:23px;font-weight:600;color:#1e2b2d}
  .apply{position:absolute;left:303px;top:1020px;font-size:20px;color:#1e2b2d}
  .contact{position:absolute;left:303px;top:1062px;font-size:12.2px;line-height:16px;color:#1e2b2d}
</style>
</head>
<body>
<div class="flyer">
  <div class="brand"><span class="brand-dot"></span><span class="brand-name">NORTHBOUND<br>PLACEMENTS</span></div>

  <svg class="flag flag-us" viewBox="0 0 84 84" role="img" aria-label="American flag">
    <defs><clipPath id="us-clip"><circle cx="42" cy="42" r="40"/></clipPath></defs>
    <g clip-path="url(#us-clip)">
      <rect width="84" height="84" fill="#fff"/>
      <rect y="0" width="84" height="6.5" fill="var(--us-red)"/>
      <rect y="13" width="84" height="6.5" fill="var(--us-red)"/>
      <rect y="26" width="84" height="6.5" fill="var(--us-red)"/>
      <rect y="39" width="84" height="6.5" fill="var(--us-red)"/>
      <rect y="52" width="84" height="6.5" fill="var(--us-red)"/>
      <rect y="65" width="84" height="6.5" fill="var(--us-red)"/>
      <rect y="78" width="84" height="6.5" fill="var(--us-red)"/>
      <rect width="38" height="45" fill="var(--us-blue)"/>
    </g>
    <circle cx="42" cy="42" r="40" fill="none" stroke="#e8e8e8" stroke-width="2"/>
  </svg>
  <svg class="flag flag-ie" viewBox="0 0 84 84" role="img" aria-label="Irish flag">
    <defs><clipPath id="ie-clip"><circle cx="42" cy="42" r="40"/></clipPath></defs>
    <g clip-path="url(#ie-clip)">
      <rect width="28" height="84" fill="var(--ie-green)"/>
      <rect x="28" width="28" height="84" fill="#fff"/>
      <rect x="56" width="28" height="84" fill="var(--ie-orange)"/>
    </g>
    <circle cx="42" cy="42" r="40" fill="none" stroke="#e8e8e8" stroke-width="2"/>
  </svg>

  <div class="photo photo-office" role="img" aria-label="Red-brick corner office building in Dublin"></div>
  <div class="photo photo-river" role="img" aria-label="Bridge over the river at dusk in Dublin"></div>
  <div class="photo photo-hall" role="img" aria-label="Columned historic building facade in Dublin"></div>

  <svg class="lines" width="785" height="1200" viewBox="0 0 785 1200">
    <path d="M477 417 H745 Q779 417 779 451 V610" fill="none" stroke="var(--rule)" stroke-width="4"/>
    <path d="M6 540 V770" fill="none" stroke="var(--rule)" stroke-width="2"/>
    <path d="M779 840 V955 Q779 990 744 990" fill="none" stroke="var(--rule)" stroke-width="4"/>
  </svg>

  <h1 class="title">Venture Lantern</h1>
  <div class="subtitle">Dublin Entrepreneur Internship Program</div>
  <div class="dates">May 31- August 9 2014</div>

  <section class="col-why">
    <h2>Why Dublin:</h2>
    <p>Dublin is at the heart of new European investment in business innovation and we can’t imagine a better place to launch your career. As the European headquarters for many of the leading tech and social media corporations, the city is gaining traction as a dynamic place to create and grow business.</p>
  </section>

  <section class="col-exp">
    <h2>The Experience:</h2>
    <p>Northbound Placements wants to help young professionals embrace Dublin’s entrepreneurial spirit for a 10-week immersion internship program into the world of entrepreneurship. Along with a full-time internship in Irish start-ups, interns will tour companies like Corvane Systems, have panel discussions with industry leaders and partake in a business competition complete with prizes.</p>
    <h2 class="inclusions">Inclusions:</h2>
    <ul>
      <li>Centralized housing in Liffey Quay College</li>
      <li>Guaranteed internship within a startup or entrepreneurial enterprise</li>
      <li>Panel discussions</li>
      <li>Site visits with companies including Corvane Systems</li>
      <li>Networking events</li>
      <li>Entrepreneurship challenge with prizes</li>
      <li>Social events and excursions</li>
      <li>24/7 on the ground staff support</li>
      <li>Career development and access to the Talentscope Profile assessment</li>
    </ul>
  </section>

  <div class="shot shot-team" role="img" aria-label="Business team presenting a laptop in front of an office sign"></div>
  <div class="shot shot-lobby" role="img" aria-label="Networking event in a modern office lobby"></div>
  <div class="shot shot-board" role="img" aria-label="Panel discussion around a boardroom table"></div>

  <div class="price">Price : $7,190</div>
  <div class="apply">Apply now at www.northboundplacements.com</div>
  <div class="contact">Northbound Placements<br>ava@northboundplacements.com<br>Contact : 1-555-014-2290</div>
</div>
</body>
</html>
```